Guarenteed! - Homepage Website Design - Coding not required- Winner to complete further pages

Hi all,

We're looking at redesigning our current website with a few adjustments to other pages but the main adjustments will be on the homepage which is what this design request is for. Please note : any of these ideas can be changed if you have something particularly different / special in mind etc.

P.S Coding is not required, just a design.

- Our website -

Our website is simply a price comparison website that allows customers to find companies within their area at the best price. The products available are mostly related to the vehicle trade and all refer to vinyl. This includes the likes of vehicle window tint, vehicle colour change vehicle wrap, vehicle signage as well as other cosmetic vinyl modifications. We allow the customer to search for their product within their chosen area and receive a list of companies who supply their product within that area. From here they can compare prices and view further details on the company.

- What we're looking to do -

We're looking first of all to adjust how the website homepage is displayed, this includes adding images and adjusting the colours that are explained below:

First of all, we look to spread out each of the 12 products (which can be seen on the website as it stands) and add an image to each of the products (all being spaced out as shown in our sketch)

We've been told the website looks too busy so we're thinking if we adjust the colours to more simplier neutral colours as well as the main focus of the website being on the 12 images, that would be great.

- Logo + Banner -

Logo to remain top left although banner may be removed / adjusted to make simplier.

- Colours -

Adjustments - Colours shades
We want the website to still look exciting but simplify the colours. Needs to be kept up to date with the colours / textures etc (bright colours to highlight keypoints)
We're still looking to use either blue or orange or maybe both to highlight these keypoints but the main website to be light colours and maybe even black on white background. The entire homepage can be adjusted colour wise if you feel it fits into your theme including menu bars, banners etc. The key is to get this right with being not too overpowering with the colours but still look interesting and up to date.

- 1 - 4 steps banner - (text may change)

This sits just under the logo and explains to the user how easy the website is to use and the steps they need to take. This may change to a 1 - 5 steps but we're looking to have this designed once the overall colours / theme of the website is sorted.

- 12 images - 4 x 3

This is the main focus of the website and will be the main focus of what the customer sees first of all. This will be where they select their product and then underneath, enter their postcode and distance they would like to search within. As explained further up, we have some of the product images available so if you can where possible add these to the design and then duplicate the images on those we currently don't have available.

- 12 Images -Titles -

These titles will be in this order from left to right and etc

- Colour Change Wrap
- Printed Vehicle Wrap
- Window Tint
- Headlight Tint
- Vehicle Signage
- Shop Signage
- Roof Vinyl Wrap
- Bonnet Vinyl Wrap
- Carbon Fibre Vinyl
- Stickerbomb Vinyl
- Clear Protective Vinyl
- Wheel Refurb

Text to be quite large, centered and with the o to the left of the title. Short titles like 'Window Tint' should fit on one line in the middle of the box where as titles such as ' Stickerbomb Vinyl Wrap' should have the 'Stickerbomb Vinyl' on the first line with the 'Wrap' on the line below. The background of this text is up to experient, might be worth just a simple colour or it might be worth using a bright blue or orange to keep in with the theme of the logo etc.

These will also have the circle tick box to the left of the title (as on the current website) where the customer clicks to select the product they have available.
We were also thinking that if when the customer ticks the circle on their selected box, the box is highlighted in some way to show this.

- Search Block -

This will appear under the 12 images and allows the customer to input their postcode and distance for the search criteria. Colours on this can of course be adjusted to keep in theme with the website.

- Under the 12 Images -

- Block underneath the 12 images and search block -

To the left will be some key bullet points about the website - maybe 4 or 5 with a green tick to the left of this. Background colour will probably be best to be a light colour, possibly grey.

Then to the right of this will appear 4 images, 2 before and 2 after when applying these products. Images to be used aren't fully decided on and we would like this stage of the design left to the end when the rest of the theme etc have been decided on.

Attached images are as follows :
- How the website looks as it stands
- The fold line on the website (obviously important)
- Our rough sketch of how we'd like the website homepage to look.
- We have 7 of the images ready that are all attached in this one file. Please duplicate the images on those that currently don't have the image available.

We will also be requesting a website developer to put this into action if our current designer falls through so please feel free to contact us if potentially interested.

The layout can change if you can think of something particular different / unique that works with this design. The main idea is to not only get the 12 products on view to the viewers but also the keypoints and before and after images.

Any questions, please ask away as we're bound to have forgotten a few things.

Thanks and good luck!

Hi all, keep the designs coming.

We haven't quite seen that extra special design we're after. As stated, we're after something fairly simple to suit the youth as well as the middle aged but we're also after something that bit special.

Colours to concentrate on are still and orange etc although feel free to use other colours if you have anything special in mind.

Please experience and we'll give you our honest feedback.

Many thanks all and good luck!

Hi all, this is a message to all the designers.

Some good designs coming in but we're still after that something special for the website design. Keep the designs coming and please feel free to experiment with the design colours, layout etc.

The basic principle of the website needs to remain regarding the 12 products, search within block and 4 steps all appearing on the homepage.

The 4 steps seems to work best when it's got text as well as some simple images next to this.

A variation with the product titles with how to display this, some designers have gone with a simple white background whereas others have gone with colours. Please experiment here and where possible, add a contract / texture to the colour. Please remember the product titles needs to be clear, centured and with the circle tick box to the left of it. 

We're after a fairly simple design although we need it to look 21st century, up to date as well as interesting. The key points straight away are the 4 steps as well as the 12 products so try to guide the viewer to these areas a little.

White background behind the 12 images seems to be a much, although a light colour could possibly work.

The keypoints underneath these 12 products are too very important as it outlines what we do etc. Tick colour can vary.

Next to these keypoints will be the 'before' and 'after' images, these images needs to be fairly small and ensure there is white background around the image itself.

Good luck all and any questions, feel free to ask away.

Thanks!

Hi,

 Thank you for your time and effort with these designs, we are very nearly there with the design but we've thought of something that may work for the homepage. A curved arrow from step 1 pointing to the products, this may or may not work but feel free to give it a go.

Many thanks,

Thank you to everyone for your time and efforts with the design. It's hugely appreciated so thank you all once again.

Wish you all the luck in the future.

```html
<!DOCTYPE html>
<html lang="en">
<head>
<meta charset="utf-8">
<title>WrapScout – Compare Vinyl Installers</title>
<link rel="stylesheet" href="https://fonts.googleapis.com/css2?family=Open+Sans:wght@400;600;700;800&display=swap">
<style>
:root{
  --navy:#263c67;
  --navy-dark:#1c2d4f;
  --orange:#f39a1e;
  --orange-dark:#e07f0c;
  --page:#ececec;
  --white:#ffffff;
  --text:#555b66;
  --muted:#8a8f98;
  --line:#d7d7d7;
}
*{box-sizing:border-box;margin:0;padding:0}
html,body{width:724px;height:1200px;overflow:hidden}
body{font-family:"Open Sans",Arial,sans-serif;background:var(--page);color:var(--text);font-size:11px}

.site-header{height:98px;background:var(--white);position:relative}
.brand{position:absolute;left:80px;top:20px;display:flex;align-items:center;gap:8px}
.brand-mark{width:34px;height:34px;border-radius:50%;background:var(--orange)}
.brand-name{font-weight:800;font-size:26px;color:var(--navy);letter-spacing:.5px}
.promo{position:absolute;left:273px;top:6px;width:439px;height:86px;background:linear-gradient(180deg,#f7a93a,var(--orange-dark));display:flex;align-items:center;padding-left:24px}
.promo-text{flex:1;text-align:center}
.promo-title{font-weight:800;color:var(--white);font-size:23px;line-height:1.05}
.promo-title .line2{display:block;background:var(--white);color:var(--orange-dark);font-size:17px;margin:4px auto 3px;width:300px;padding:2px 0}
.promo-sub{color:var(--white);font-size:11px;font-weight:600}
.promo-art{width:78px;height:70px;margin:0 12px;border-radius:6px;background:linear-gradient(135deg,#f6d38c,#c9852a)}

.main-nav{height:36px;background:var(--navy);display:flex;align-items:center;padding:0 72px 0 80px}
.main-nav a{color:var(--white);text-decoration:none;font-size:10px;font-weight:700;margin-right:22px}
.main-nav a.active{color:var(--orange)}
.social{margin-left:auto;display:flex;gap:6px}
.social span{width:20px;height:20px;border-radius:50%;background:var(--white)}

.section-title{text-align:center;color:var(--orange);font-weight:800;font-size:13px;letter-spacing:.5px}
.how{padding-top:14px;height:202px}
.steps{display:flex;gap:10px;margin:10px 0 0 80px;width:567px}
.step{width:134px;height:118px;background:var(--navy);position:relative;text-align:center;color:var(--white);font-size:9.5px;line-height:1.35;padding-top:14px}
.step-num{position:absolute;left:0;top:0;width:34px;height:34px;background:var(--orange);clip-path:polygon(0 0,100% 0,0 100%);}
.step-num b{position:absolute;left:5px;top:2px;font-size:13px}
.step-icon{width:56px;height:50px;margin:0 auto 8px;border-radius:6px}
.step p{padding:0 10px}

.categories{background:var(--page);height:568px}
.cat-grid{display:grid;grid-template-columns:repeat(4,133px);gap:22px 12px;margin:12px 0 0 80px}
.cat-card{height:152px;background:var(--white);border:1px solid var(--line);display:flex;flex-direction:column}
.cat-photo{flex:1;margin:8px;border-radius:2px}
.cat-label{height:30px;background:var(--navy);display:flex;align-items:center;justify-content:space-between;padding:0 6px 0 8px;color:var(--white);font-size:9px}
.cat-label svg{flex:none}

.highlights{background:var(--white);height:194px;display:flex;padding:22px 0 0 80px}
.points{list-style:none;width:330px;padding-top:16px}
.points li{display:flex;align-items:center;gap:8px;font-size:9.5px;margin-bottom:13px;color:var(--text)}
.compare{display:flex;gap:22px;margin-left:98px}
.compare-col h3{font-size:12px;font-weight:700;color:#333;margin-bottom:6px}
.compare-col .shot{width:86px;height:64px;margin-bottom:10px;border:4px solid var(--white);box-shadow:0 0 0 1px var(--line)}

.newsletter{height:60px;background:var(--navy-dark);display:flex;align-items:center;padding:0 72px 0 80px;gap:18px}
.newsletter h2{color:var(--white);font-size:13px;font-weight:700}
.newsletter .field{flex:1;height:26px;background:var(--navy);border:1px solid #3a5286;color:#9aa8c4;font-size:10px;display:flex;align-items:center;padding-left:8px}
.newsletter .btn{background:var(--orange);color:var(--white);font-weight:700;font-size:11px;height:26px;padding:0 12px;display:flex;align-items:center}

.site-footer{height:62px;background:var(--white);text-align:center;padding-top:14px;font-size:9px;color:var(--muted)}
.site-footer nav a{color:var(--text);text-decoration:none;margin:0 6px}
.site-footer p{margin-top:6px}
</style>
</head>
<body>
<header class="site-header">
  <div class="brand"><span class="brand-mark"></span><span class="brand-name">WrapScout</span></div>
  <div class="promo">
    <div class="promo-text">
      <div class="promo-title">FIND A PROFESSIONAL<span class="line2">VINYL INSTALLER TODAY</span></div>
      <div class="promo-sub">Search &amp; Save In Seconds</div>
    </div>
    <div class="promo-art" role="img" aria-label="Illustration of a folded map with a location pin"></div>
  </div>
</header>

<nav class="main-nav">
  <a href="#" class="active">HOME</a>
  <a href="#">ABOUT US</a>
  <a href="#">CONTACT US</a>
  <a href="#">BLOG</a>
  <a href="#">LIST YOUR COMPANY HERE</a>
  <div class="social"><span></span><span></span></div>
</nav>

<section class="how">
  <h2 class="section-title">HOW IT WORKS</h2>
  <div class="steps">
    <div class="step"><div class="step-num"><b>1</b></div><div class="step-icon" role="img" aria-label="Cardboard box icon" style="background:linear-gradient(135deg,#e7b779,#a9703a)"></div><p>Select Chosen<br>Products</p></div>
    <div class="step"><div class="step-num"><b>2</b></div><div class="step-icon" role="img" aria-label="Map with location pin icon" style="background:linear-gradient(135deg,#f2f2f2,#8fc1e8)"></div><p>Input Postcode, Distance<br>+<br>Search</p></div>
    <div class="step"><div class="step-num"><b>3</b></div><div class="step-icon" role="img" aria-label="Buildings with price tag icon" style="background:linear-gradient(135deg,#d9e3ea,#6c8da3)"></div><p>Compare Companies<br>+<br>Prices</p></div>
    <div class="step"><div class="step-num"><b>4</b></div><div class="step-icon" role="img" aria-label="Office towers icon" style="background:linear-gradient(135deg,#e8f0f5,#8fa9bb)"></div><p>Compare Chosen<br>Companies</p></div>
  </div>
</section>

<section class="categories">
  <h2 class="section-title">CATEGORIES</h2>
  <div class="cat-grid">
    <div class="cat-card"><div class="cat-photo" role="img" aria-label="Car with colour change wrap" style="background:linear-gradient(135deg,#f2f2f2,#c9302c)"></div><div class="cat-label">Colour Change Wrap<svg width="16" height="16" viewBox="0 0 16 16"><circle cx="8" cy="8" r="8" fill="#fff"/><path d="M6.5 4.5 10 8l-3.5 3.5" stroke="#263c67" stroke-width="2" fill="none"/></svg></div></div>
    <div class="cat-card"><div class="cat-photo" role="img" aria-label="Van with printed vehicle wrap" style="background:linear-gradient(135deg,#f4f4f4,#5aa14a)"></div><div class="cat-label">Printed Vehicle Wrap<svg width="16" height="16" viewBox="0 0 16 16"><circle cx="8" cy="8" r="8" fill="#fff"/><path d="M6.5 4.5 10 8l-3.5 3.5" stroke="#263c67" stroke-width="2" fill="none"/></svg></div></div>
    <div class="cat-card"><div class="cat-photo" role="img" aria-label="Cars with tinted windows" style="background:linear-gradient(135deg,#f4f4f4,#3f9a3a)"></div><div class="cat-label">Window Tint<svg width="16" height="16" viewBox="0 0 16 16"><circle cx="8" cy="8" r="8" fill="#fff"/><path d="M6.5 4.5 10 8l-3.5 3.5" stroke="#263c67" stroke-width="2" fill="none"/></svg></div></div>
    <div class="cat-card"><div class="cat-photo" role="img" aria-label="Dark car with tinted headlights" style="background:linear-gradient(135deg,#f4f4f4,#2c2c2c)"></div><div class="cat-label">Headlight Tint<svg width="16" height="16" viewBox="0 0 16 16"><circle cx="8" cy="8" r="8" fill="#fff"/><path d="M6.5 4.5 10 8l-3.5 3.5" stroke="#263c67" stroke-width="2" fill="none"/></svg></div></div>

    <div class="cat-card"><div class="cat-photo" role="img" aria-label="White van with signage" style="background:linear-gradient(135deg,#f6f6f6,#b9bfc6)"></div><div class="cat-label">Vehicle Signage<svg width="16" height="16" viewBox="0 0 16 16"><circle cx="8" cy="8" r="8" fill="#fff"/><path d="M6.5 4.5 10 8l-3.5 3.5" stroke="#263c67" stroke-width="2" fill="none"/></svg></div></div>
    <div class="cat-card"><div class="cat-photo" role="img" aria-label="Shop front with signage" style="background:linear-gradient(135deg,#e6e6e6,#5d5d5d)"></div><div class="cat-label">Shop Signage<svg width="16" height="16" viewBox="0 0 16 16"><circle cx="8" cy="8" r="8" fill="#fff"/><path d="M6.5 4.5 10 8l-3.5 3.5" stroke="#263c67" stroke-width="2" fill="none"/></svg></div></div>
    <div class="cat-card"><div class="cat-photo" role="img" aria-label="Car with black vinyl roof" style="background:linear-gradient(135deg,#f4f4f4,#6b6b6b)"></div><div class="cat-label">Roof Vinyl Wrap<svg width="16" height="16" viewBox="0 0 16 16"><circle cx="8" cy="8" r="8" fill="#fff"/><path d="M6.5 4.5 10 8l-3.5 3.5" stroke="#263c67" stroke-width="2" fill="none"/></svg></div></div>
    <div class="cat-card"><div class="cat-photo" role="img" aria-label="Car with vinyl wrapped bonnet" style="background:linear-gradient(135deg,#f4f4f4,#8d8d8d)"></div><div class="cat-label">Bonnet Vinyl Wrap<svg width="16" height="16" viewBox="0 0 16 16"><circle cx="8" cy="8" r="8" fill="#fff"/><path d="M6.5 4.5 10 8l-3.5 3.5" stroke="#263c67" stroke-width="2" fill="none"/></svg></div></div>

    <div class="cat-card"><div class="cat-photo" role="img" aria-label="Car with carbon fibre vinyl" style="background:linear-gradient(135deg,#f4f4f4,#3a3a3a)"></div><div class="cat-label">Carbon Vinyl Wrap<svg width="16" height="16" viewBox="0 0 16 16"><circle cx="8" cy="8" r="8" fill="#fff"/><path d="M6.5 4.5 10 8l-3.5 3.5" stroke="#263c67" stroke-width="2" fill="none"/></svg></div></div>
    <div class="cat-card"><div class="cat-photo" role="img" aria-label="Car covered in stickerbomb vinyl" style="background:linear-gradient(135deg,#e9d36a,#c24f7c)"></div><div class="cat-label">Sticker Bombs Vinyl<svg width="16" height="16" viewBox="0 0 16 16"><circle cx="8" cy="8" r="8" fill="#fff"/><path d="M6.5 4.5 10 8l-3.5 3.5" stroke="#263c67" stroke-width="2" fill="none"/></svg></div></div>
    <div class="cat-card"><div class="cat-photo" role="img" aria-label="White car with clear protective vinyl" style="background:linear-gradient(135deg,#f6f6f6,#b8bcc2)"></div><div class="cat-label">Clear Protective Vinyl<svg width="16" height="16" viewBox="0 0 16 16"><circle cx="8" cy="8" r="8" fill="#fff"/><path d="M6.5 4.5 10 8l-3.5 3.5" stroke="#263c67" stroke-width="2" fill="none"/></svg></div></div>
    <div class="cat-card"><div class="cat-photo" role="img" aria-label="Car with refurbished wheels" style="background:linear-gradient(135deg,#f4f4f4,#5b4a36)"></div><div class="cat-label">Wheel Refurbs<svg width="16" height="16" viewBox="0 0 16 16"><circle cx="8" cy="8" r="8" fill="#fff"/><path d="M6.5 4.5 10 8l-3.5 3.5" stroke="#263c67" stroke-width="2" fill="none"/></svg></div></div>
  </div>
</section>

<section class="highlights">
  <ul class="points">
    <li><svg width="14" height="14" viewBox="0 0 14 14"><circle cx="7" cy="7" r="7" fill="#f39a1e"/><path d="M3.8 7.2 6 9.3l4.2-4.6" stroke="#fff" stroke-width="1.8" fill="none"/></svg>Get all prices from local installers in one simple place</li>
    <li><svg width="14" height="14" viewBox="0 0 14 14"><circle cx="7" cy="7" r="7" fill="#f39a1e"/><path d="M3.8 7.2 6 9.3l4.2-4.6" stroke="#fff" stroke-width="1.8" fill="none"/></svg>Compare trusted vinyl companies near you in seconds</li>
    <li><svg width="14" height="14" viewBox="0 0 14 14"><circle cx="7" cy="7" r="7" fill="#f39a1e"/><path d="M3.8 7.2 6 9.3l4.2-4.6" stroke="#fff" stroke-width="1.8" fill="none"/></svg>Every listed installer is checked and rated by customers</li>
    <li><svg width="14" height="14" viewBox="0 0 14 14"><circle cx="7" cy="7" r="7" fill="#f39a1e"/><path d="M3.8 7.2 6 9.3l4.2-4.6" stroke="#fff" stroke-width="1.8" fill="none"/></svg>Free to use with no hidden fees at all</li>
  </ul>
  <div class="compare">
    <div class="compare-col">
      <h3>Before</h3>
      <div class="shot" role="img" aria-label="White car before wrapping" style="background:linear-gradient(135deg,#eef0f2,#9aa3ab)"></div>
      <div class="shot" role="img" aria-label="Car before window tint" style="background:linear-gradient(135deg,#e9ecef,#7d8894)"></div>
    </div>
    <div class="compare-col">
      <h3>After</h3>
      <div class="shot" role="img" aria-label="Car after red colour change wrap" style="background:linear-gradient(135deg,#f2e3e3,#b52a2a)"></div>
      <div class="shot" role="img" aria-label="Car after window tint" style="background:linear-gradient(135deg,#e4e6e8,#2f3338)"></div>
    </div>
  </div>
</section>

<section class="newsletter">
  <h2>JOIN OUR MAIL LISTINGS</h2>
  <div class="field">Enter your email</div>
  <div class="btn">SUBSCRIBE</div>
</section>

<footer class="site-footer">
  <nav><a href="#">Home</a>|<a href="#">About Us</a>|<a href="#">Contact Us</a>|<a href="#">Blog</a>|<a href="#">List Your Company Here</a></nav>
  <p>Copyright ©2013 Company Name – All rights reserved</p>
</footer>
</body>
</html>
```